Drinking Water Protection Postcard Series

Design a series of 3 themed postcards that will be mailed in succession for a pilot project. Audience: to reach water operators who are responsible for managing very small public water systems (serving less than 1000 people in Pennsylvania). Purpose: Encourage small water systems to enter into a voluntary program known as "Brightmere Wellhead Care for Hamlet Utilities" that is available at no out of pocket cost from Harlow Bureau of Habitat Stewardship (HBHS). Source Water Protection helps protect public health by preventing contaminants from entering the rivers, streams and groundwater on which the public depends for source of drinking water. Source water protection safeguards public health, makes efficient use of limited financial resources (prevention is cheaper than water treatment or loss of a well), and has a positive impact on the environment as a whole. Slogan is: "Safe Drinking Water Starts at the Source." A Source Water Protection program maps out where your drinking water comes from, shows ways to stop pollution before it starts, and helps plan for water emergencies.
We have a logo for the program (and more info) that can be seen at www.brightmerewellhead.example.org and is attached. We are considering a tag line like: "Show you care. Get a Source Water Protection Plan for your water system." Would like to see designs that use the colors blue and green, and families, a glass of water to communicate good stewardship is smart business. Many small water systems are privately owned mobile home parks.
Reason: Some designers emailed they were going to submit, but I don't believe we received their designs yet. Thank you all for your work.
Sorry for the delay in responding. 9/30 was year end for us which took priority over our new projects. We are getting back on track and have sent designs out for review and input from our small nonprofit team. Thanks for your patience, and if you have had any other inspirations that may encourage water systems to protect their raw drinking water sources out in the watershed, please send them along; we will be reviewing this week. Preventing pollution up front is much cheaper and safer than trying to treat for every contaminant at the water treatment plant. Many thanks.
about 95% mail blue collar adults; aged 25 - 65 in more rural areas of Pennsylvania.
Water Treatment

```html
<!DOCTYPE html>
<html lang="en">
<head>
<meta charset="utf-8">
<title>Safe Drinking Water Starts at the Source – Postcard</title>
<link rel="stylesheet" href="https://fonts.googleapis.com/css2?family=Roboto:ital,wght@0,300;0,400;0,700;1,400&display=swap">
<style>
  :root {
    --deep-blue: #0b3f8c;
    --mid-blue: #1565c0;
    --bright-blue: #2f86d6;
    --header-blue: #1a4d9e;
    --band-blue: rgba(6, 45, 110, 0.35);
    --teal: #13999a;
    --sky: #a9d8ee;
    --pale-green: #9fd08a;
    --white: #ffffff;
    --brand-ink: #1a4d9e;
  }
  * { margin: 0; padding: 0; box-sizing: border-box; }
  html, body { width: 1200px; height: 772px; overflow: hidden; background: var(--white); }
  body { font-family: "Roboto", Arial, sans-serif; color: var(--white); }

  .postcard { position: relative; width: 1200px; height: 772px; overflow: hidden; }

  .splash-photo {
    position: absolute; inset: 0;
    background:
      radial-gradient(ellipse 500px 380px at 850px 380px, var(--bright-blue), transparent 75%),
      linear-gradient(180deg, var(--mid-blue) 0%, var(--deep-blue) 100%);
  }

  .droplet-panel { position: absolute; left: 0; top: 0; width: 480px; height: 772px; }

  .header-box {
    position: absolute; left: 468px; top: 0; width: 617px; height: 222px;
    background: var(--header-blue);
    border-bottom-right-radius: 22px;
    text-align: center;
    padding-top: 28px; padding-left: 0;
  }
  .header-box .lead { font-weight: 300; font-size: 40px; line-height: 46px; }
  .header-box .call { font-weight: 700; font-size: 35px; line-height: 46px; }

  .leaf-drop {
    position: absolute; left: 265px; top: 129px; width: 306px; height: 306px;
    border-radius: 50%; border: 5px solid var(--white);
    background: linear-gradient(180deg, var(--pale-green) 0%, var(--sky) 55%, var(--sky) 100%);
  }

  .brand-tag {
    position: absolute; left: 55px; top: 35px; width: 207px; height: 152px;
    background: var(--white); border-radius: 12px;
    display: flex; align-items: center; justify-content: center; gap: 10px;
    padding: 0 14px;
  }
  .brand-tag .dot { width: 16px; height: 16px; border-radius: 50%; background: var(--brand-ink); flex: none; }
  .brand-tag .name { color: var(--brand-ink); font-weight: 700; font-size: 20px; line-height: 24px; }

  .program-band {
    position: absolute; left: 0; top: 470px; width: 462px; height: 185px;
    background: var(--teal);
    text-align: right; padding: 22px 42px 0 0;
    font-size: 18px; line-height: 28.5px;
  }
  .program-band em { font-style: italic; }

  .slogan {
    position: absolute; left: 612px; top: 384px;
    font-weight: 300; font-size: 82px; line-height: 88px; letter-spacing: -0.5px;
  }

  .web-band {
    position: absolute; left: 440px; top: 655px; width: 760px; height: 62px;
    background: var(--band-blue);
  }
  .web-address {
    position: absolute; left: 470px; top: 664px;
    font-weight: 400; font-size: 29px; line-height: 40px; letter-spacing: 1.4px;
    white-space: nowrap;
  }
</style>
</head>
<body>
<main class="postcard">
  <div class="splash-photo" role="img" aria-label="Photo of a water droplet splashing into a deep blue pool"></div>

  <svg class="droplet-panel" viewBox="0 0 480 772" role="img" aria-label="Close-up photo of dew drops clinging to fine white fibres">
    <defs>
      <linearGradient id="frostGrad" x1="0" y1="0" x2="1" y2="1">
        <stop offset="0" stop-color="#6f9fc8"/>
        <stop offset="0.45" stop-color="#e8f2fa"/>
        <stop offset="1" stop-color="#5c8dbb"/>
      </linearGradient>
    </defs>
    <path d="M0 0 H448 C462 260 470 520 430 772 H0 Z" fill="url(#frostGrad)"/>
  </svg>

  <header class="header-box">
    <p class="lead">Show you care.</p>
    <p class="call">Get a Source Water<br>Protection Plan for your<br>water system</p>
  </header>

  <div class="leaf-drop" role="img" aria-label="Photo of a clear green water drop hanging from a blade of grass"></div>

  <div class="brand-tag">
    <span class="dot"></span>
    <span class="name">Brightmere Wellhead Care</span>
  </div>

  <section class="program-band">
    <p>Enter into a voluntary program known<br>
    as <em>Brightmere Wellhead Care for</em><br>
    <em>Hamlet Utilities</em> that is available at no<br>
    out of pocket cost from Harlow Bureau of<br>
    Habitat Stewardship (HBHS)</p>
  </section>

  <h1 class="slogan">Safe Drinking<br>Water Starts<br>at the Source</h1>

  <div class="web-band"></div>
  <p class="web-address">Visit: www.brightmerewellhead.example.org</p>
</main>
</body>
</html>
```